Create a pouch design for a new sports supplement product

Dimensions are 235mm (width) x 335mm (length) x 110mm (gusset)
File 1 - Extension of design brief please read both briefs
File 2 - Is 2 potential pouches this is just to give you a better example of size the dimensions are for the pouch on the right. This picture is not to give you design ideas as I am not very keen on either of these designs.
We need a design to be printed onto the pouches of our whey protein product. The brand name is 'Stellar Fuelworks' and needs to be displayed on the packaging either just writing or a simple logo design. I am not the most creative person in the world but have put together a more detailed brief listing some of the key information that needs to be included on the pouch (See attachment) Please feel free if you have experience of this the sports supplement market or have different ideas then please feel free to explore them.
The pouch would either be printed straight onto the pouch, or possibly just a printed label (front & back) to be stuck onto the pouch. Please design either or both.
Open to different colour schemes. Design has to be modern looking and eye-catching.
Some key points;
High quality whey protein concentrate
All Natural
Soy free
Great tasting
Please google image search 'protein pouches' to see other designs if your not familiar with the sports supplement market.
Any questions feel free to ask.
Updates
Hi, Thanks for all your design! I am really busy at the moment so haven't had chance to give feedback and have a proper look through all the designs. I have extended the time frame to give myself chance to give proper feedback and see any changes needed. Expect feedback sunday at the latest, and I will be pick a design early next week.
Target Market(s)
Sports supplement market. Product is a whey protein shake
Industry/Entity Type
Nutrition
Look and feel
Each slider illustrates characteristics of the customer's brand and the style your logo design should communicate.

```html
<!DOCTYPE html>
<html lang="en">
<head>
<meta charset="utf-8">
<title>Stellar Fuelworks Whey Protein – Pouch Design</title>
<link rel="stylesheet" href="https://fonts.googleapis.com/css2?family=Montserrat:wght@600;700&family=Raleway:wght@300;400;500&family=Arimo:wght@400;700&display=swap">
<style>
:root{
  --green:#5fcb00;
  --gold:#c9b45c;
  --red:#e5321d;
  --pouch:#f4f5f5;
  --band:#cfd1d2;
  --ink:#111;
  --muted:#666;
  --bg:#ffffff;
}
*{box-sizing:border-box;margin:0;padding:0}
html,body{width:1200px;height:1000px;overflow:hidden;background:var(--bg)}
.canvas{position:relative;width:1200px;height:1000px;font-family:"Raleway",sans-serif}
.size-tag{position:absolute;left:0;top:36px;width:307px;height:64px;background:var(--green);color:#fff;font:400 40px/64px "Raleway",sans-serif;padding-left:16px}
.side-label{position:absolute;top:862px;font:700 36px "Montserrat",sans-serif;color:var(--green)}
.side-label.front{left:268px}.side-label.back{left:883px}

.pouch{position:absolute;top:185px;width:490px;height:640px;background:var(--pouch);border-radius:14px 14px 30px 30px;overflow:hidden;border:1px solid #e2e3e3}
.pouch.front{left:65px}.pouch.back{left:645px}
.seal-line{position:absolute;left:10px;right:10px;top:22px;border-top:3px dashed var(--green)}
.tear-tab{position:absolute;right:8px;top:34px;width:270px;height:28px;background:var(--green);clip-path:polygon(8% 0,100% 0,100% 100%,0 100%);color:#fff;font:400 18px/28px "Raleway",sans-serif;letter-spacing:1px;text-align:right;padding-right:22px}
.zip-band{position:absolute;left:0;right:0;top:72px;height:12px;background:var(--band)}
.base-line{position:absolute;left:0;right:0;height:2px}
.base-line.green{top:585px;background:var(--green)}
.base-line.gold{top:620px;background:var(--gold)}

.brand{position:absolute;font-family:"Montserrat",sans-serif;font-weight:700;color:var(--green);line-height:1}
.front .brand{left:33px;top:120px;font-size:34px}
.back .brand{left:33px;top:112px;font-size:19px}
.brand sup{font-size:.4em;vertical-align:top}

.product-name{position:absolute;color:var(--gold);font-weight:300;line-height:1}
.front .product-name{left:45px;top:258px;font-size:60px;letter-spacing:2px}
.front .product-name .rule{display:block;width:270px;height:3px;background:var(--green);margin:6px 0 4px}
.back .product-name{left:35px;top:158px;font-size:24px}
.back .product-name .rule{display:block;width:112px;height:2px;background:var(--green);margin:2px 0}

.claims{position:absolute;left:55px;top:380px;list-style:none;font:700 15px/1.4 "Arimo",sans-serif}
.claims li{padding-left:14px;position:relative}
.claims li::before{content:"";position:absolute;left:0;top:7px;width:10px;height:5px;background:currentColor}
.claims li:nth-child(odd){color:var(--green)}
.claims li:nth-child(even){color:var(--gold)}

.flavour-vertical{position:absolute;left:340px;top:570px;transform:rotate(-90deg);transform-origin:0 0;color:var(--red);font-weight:400;font-size:66px;letter-spacing:4px;white-space:nowrap;line-height:1}
.flavour-rule{position:absolute;left:417px;top:185px;width:3px;height:370px;background:var(--red)}
.flavour-word{position:absolute;left:425px;top:262px;transform:rotate(-90deg);transform-origin:0 0;color:var(--red);font-size:14px;letter-spacing:2px}
.net-weight{position:absolute;left:143px;top:522px;color:var(--gold);font-size:24px;line-height:1}
.net-weight small{display:block;color:var(--green);font-size:16px;font-weight:500;margin-top:2px}

.flavour-inline{position:absolute;left:168px;top:178px;color:var(--red);font-size:17px;letter-spacing:1px;text-decoration:underline;text-underline-offset:3px}
.flavour-inline small{display:block;font-size:5px;text-align:right;text-decoration:none}
.intro{position:absolute;left:35px;top:218px;width:405px;color:var(--green);font:400 11px/1.05 "Arimo",sans-serif}

.nutrition{position:absolute;left:38px;top:275px;width:160px;border:1px solid var(--ink);padding:3px;font:400 6.5px/1.15 "Arimo",sans-serif;color:var(--ink);background:#fff}
.nutrition h3{font:700 14px/1 "Arimo",sans-serif}
.nutrition .row{display:flex;justify-content:space-between;border-top:1px solid #999}
.nutrition .thick{border-top:3px solid var(--ink)}
.nutrition .indent{padding-left:6px}
.nutrition b{font-weight:700}
.nutrition p{border-top:1px solid #999;margin-top:1px}

.info{position:absolute;left:210px;top:275px;width:240px;color:var(--green);font:400 10px/1.15 "Arimo",sans-serif}
.info p{margin-bottom:10px}
.legal{position:absolute;left:212px;top:408px;width:240px;color:var(--muted);font:400 7px/1.5 "Arimo",sans-serif}
.connect{position:absolute;left:62px;top:490px;color:var(--green);font:400 11px/1.1 "Arimo",sans-serif}
.connect b{font-weight:700}
.social{position:absolute;left:62px;top:518px;display:flex;gap:5px}
.social span{width:29px;height:28px;background:var(--green)}
</style>
</head>
<body>
<div class="canvas">
  <div class="size-tag">5x7 zip pouch</div>

  <section class="pouch front">
    <div class="seal-line"></div>
    <div class="tear-tab">TEAR HERE &amp; RESEAL</div>
    <div class="zip-band"></div>
    <div class="brand">STELLAR<br>FUELWORKS<sup>TM</sup></div>
    <h1 class="product-name">WHEY<span class="rule"></span>PROTEIN</h1>
    <ul class="claims">
      <li>80% high quality protein content</li>
      <li>No artificial Flavours</li>
      <li>Excellent Amino acid profile</li>
      <li>Soy free</li>
    </ul>
    <div class="flavour-vertical">STRAWBERRY</div>
    <div class="flavour-rule"></div>
    <div class="flavour-word">FLAVOUR</div>
    <div class="net-weight">909g<small>30 servings</small></div>
    <div class="base-line green"></div>
    <div class="base-line gold"></div>
  </section>

  <section class="pouch back">
    <div class="seal-line"></div>
    <div class="tear-tab">TEAR HERE &amp; RESEAL</div>
    <div class="zip-band"></div>
    <div class="brand">STELLAR<br>FUELWORKS<sup>TM</sup></div>
    <h2 class="product-name">WHEY<span class="rule"></span>PROTEIN</h2>
    <div class="flavour-inline">STRAWBERRY<small>FLAVOUR</small></div>
    <p class="intro">Stellar Fuelworks' natural whey protein is a very high quality 100% natural instant whey protein concentrate impressively providing 80% protein content making this the perfect supplement to aid muscular growth and repair. In addition this all the ingredients are natural but yet still providing a great taste which will make you want more</p>

    <div class="nutrition">
      <h3>Nutrition Facts</h3>
      <div>Serving Size: 4 FL. OZ. (120mL)<br>Servings Per Bottle: 1</div>
      <div class="row thick"><b>Amount Per Serving</b></div>
      <div class="row"><span>Calories 130</span><span>Calories from Fat 0</span></div>
      <div class="row thick"><span></span><b>% Daily Value*</b></div>
      <div class="row"><span><b>Total Fat</b> 0g</span><span>0%</span></div>
      <div class="row indent"><span>Saturated Fat 0g</span><span>0%</span></div>
      <div class="row indent"><span>Trans Fat 0g</span><span>0%</span></div>
      <div class="row"><span><b>Cholesterol</b> 0mg</span><span>0%</span></div>
      <div class="row"><span><b>Sodium</b> 90mg</span><span>4%</span></div>
      <div class="row"><span><b>Potassium</b> 120mg</span><span>4%</span></div>
      <div class="row"><span><b>Total Carbohydrate</b> 0g</span><span>0%</span></div>
      <div class="row indent"><span>Dietary Fiber 0g</span><span>0%</span></div>
      <div class="row indent"><span>Sugars 0g</span><span></span></div>
      <div class="row"><span><b>Protein</b> 32g</span><span>64%</span></div>
      <div class="row thick"><span>Vitamin A &nbsp;0%</span><span>Vitamin C &nbsp;0%</span></div>
      <div class="row"><span>Calcium &nbsp;9%</span><span>Iron &nbsp;0%</span></div>
      <p>*Percent Daily Values are based on a 2,000 calorie diet. Your daily values may be higher or lower depending on your caloric needs.</p>
    </div>

    <div class="info">
      <p>Ingredients;<br>Whey protein concentrate 80%, Flavouring, sweetener, colour, sunflower lecithin.</p>
      <p>Storage – Store in a cool dry place</p>
      <p>Serving suggestions – Mix 25g with 150-250ml of water or milk, consume 1-4 times daily and ideally straight after working out. The less liquid, the thicker the shake.</p>
    </div>
    <p class="legal">Do not exceed serving suggestion, and always consult a doctor before use. Natural whey protein should be consumed alongside a well balanced healthy diet and training programme. For any enquiries to see website. UK manufactured. Stellar Fuelworks, unit 4, orbit yard, Bristol, BS9 4QT, UK</p>

    <div class="connect">(Stay updated/stay connected)<br><b>Stellar-Fuelworks.eu</b></div>
    <div class="social" aria-label="Social channels"><span></span><span></span><span></span><span></span><span></span></div>
    <div class="base-line green"></div>
    <div class="base-line gold"></div>
  </section>

  <div class="side-label front">FRONT</div>
  <div class="side-label back">BACK</div>
</div>
</body>
</html>
```